New layout on letterheads, businesscards, flyers, brochures etc.

Dear Sir,
We would like to change our layout a bit. We would like to have the same look on everything we make and still keep our logo. We would like some suggestions suitable for a company like ours, where solar systems, heat pumps and LED lighting is reflected. We like our blue colour in our logo (#009ddf) and some of the black reflected in our solar panels and we like the solar cell (almost square with soft corners). We like soft lines, clean look and reflecting expensive solar panels from the very best distributors (TK, Hokurazu, Brightmere Energy etc.). We want a light, soft, exclusive and expensive look to it all. We need this for business cards, letterhead/bottom, flyers, brochures and stickers etc.
Thank you in advance.

Ulvix
Bakkevej 12 B
8261 Ikast
Denmark

info@ulvix.dk
www.ulvix.dk

```html
<!DOCTYPE html>
<html lang="en">
<head>
<meta charset="utf-8">
<title>Ulvix letterhead proposals</title>
<link rel="stylesheet" href="https://fonts.googleapis.com/css2?family=Open+Sans:wght@400;600;700;800&display=swap">
<style>
  :root {
    --canvas: #ffffff;
    --frame: #e4e4e4;
    --ink: #3a3a3a;
    --ink-soft: #555555;
    --brand-blue: #009ddf;
    --dark-top: #3b3b3b;
    --dark-bottom: #8e8e8e;
    --light-band: #e1f1fb;
    --rule-dark: #9a9a9a;
    --rule-light: #8aa7b8;
    --logo-grey: #a7a9ab;
    --partner-red: #d4262c;
    --partner-grey: #555555;
  }
  * { box-sizing: border-box; margin: 0; padding: 0; }
  html, body { width: 1200px; height: 902px; overflow: hidden; background: var(--canvas); }
  body { font-family: "Open Sans", Arial, sans-serif; color: var(--ink); position: relative; }

  .sheet-frame { position: absolute; left: 2px; top: 2px; width: 1196px; height: 898px; border: 1px solid var(--frame); }

  .letterhead { position: absolute; top: 64px; width: 553px; height: 781px; background: #fff; border: 2px solid var(--frame); }
  .letterhead--dark { left: 43px; }
  .letterhead--light { left: 615px; }

  .header-band { position: absolute; left: 0; top: 0; width: 100%; height: 73px; }
  .letterhead--dark .header-band { background: linear-gradient(180deg, var(--dark-top) 0%, #4a4a4a 40%, var(--dark-bottom) 100%); color: #fff; }
  .letterhead--light .header-band { background: var(--light-band); color: var(--ink); }

  .contact { position: absolute; font-size: 7px; line-height: 10px; font-weight: 400; }
  .contact--address { left: 120px; top: 27px; }
  .contact--phone { left: 183px; top: 25px; }
  .contact--web { left: 272px; top: 36px; font-weight: 700; }

  .divider { position: absolute; top: 0; width: 1px; height: 55px; }
  .letterhead--dark .divider { background: var(--rule-dark); }
  .letterhead--light .divider { background: var(--rule-light); }
  .divider--one { left: 171px; }
  .divider--two { left: 256px; }

  .brand { position: absolute; left: 408px; top: 18px; display: flex; align-items: center; gap: 6px; }
  .brand-mark { width: 16px; height: 16px; border-radius: 4px; background: var(--brand-blue); }
  .brand-name { font-size: 30px; font-weight: 800; letter-spacing: 1px; line-height: 1; }
  .letterhead--dark .brand-name { color: #ffffff; }
  .letterhead--light .brand-name { color: var(--logo-grey); }

  .footer { position: absolute; left: 0; bottom: 18px; width: 100%; height: 40px; }
  .tagline { position: absolute; left: 31px; top: 0; font-size: 7px; letter-spacing: 2.6px; color: var(--ink-soft); }
  .product-line { position: absolute; left: 47px; top: 13px; font-size: 9px; color: var(--ink); }

  .partners { position: absolute; left: 268px; top: 2px; height: 26px; display: flex; align-items: center; gap: 12px; }
  .partner { display: flex; align-items: center; gap: 4px; font-weight: 700; }
  .partner-dot { width: 13px; height: 13px; border-radius: 50%; background: var(--partner-red); }
  .partner-square { width: 11px; height: 11px; background: var(--partner-grey); }
  .partner--tk { font-size: 11px; color: var(--partner-grey); }
  .partner--brightmere { font-size: 6px; line-height: 7px; color: var(--partner-red); width: 46px; }
  .partner--varnholt { font-size: 12px; color: var(--partner-red); }
  .partner--kestrel { font-size: 7px; color: var(--partner-red); }
  .partner--lumora { font-size: 7px; color: var(--partner-grey); }
</style>
</head>
<body>
  <div class="sheet-frame"></div>

  <section class="letterhead letterhead--dark">
    <header class="header-band">
      <p class="contact contact--address">Bakkevej 12 B<br>8261 Ikast<br>Denmark</p>
      <span class="divider divider--one"></span>
      <p class="contact contact--phone">P: +45 71 38 52 90<br>info@ulvix.dk<br>CVR: DK-48127036</p>
      <span class="divider divider--two"></span>
      <p class="contact contact--web">www.ulvix.dk</p>
      <div class="brand"><span class="brand-mark"></span><span class="brand-name">Ulvix</span></div>
    </header>
    <footer class="footer">
      <p class="tagline">Wholesaler in Energy Optimization Product</p>
      <p class="product-line">Photovoltaics · LED · Heat Pumps · Jet Towels</p>
      <div class="partners">
        <span class="partner partner--tk"><span class="partner-dot"></span>TK</span>
        <span class="partner partner--brightmere">Brightmere Energy</span>
        <span class="partner partner--varnholt">Varnholt</span>
        <span class="partner partner--kestrel"><span class="partner-dot"></span>Kestrel</span>
        <span class="partner partner--lumora"><span class="partner-square"></span>Lumora</span>
      </div>
    </footer>
  </section>

  <section class="letterhead letterhead--light">
    <header class="header-band">
      <p class="contact contact--address">Bakkevej 12 B<br>8261 Ikast<br>Denmark</p>
      <span class="divider divider--one"></span>
      <p class="contact contact--phone">P: +45 71 38 52 90<br>info@ulvix.dk<br>CVR: DK-48127036</p>
      <span class="divider divider--two"></span>
      <p class="contact contact--web">www.ulvix.dk</p>
      <div class="brand"><span class="brand-mark"></span><span class="brand-name">Ulvix</span></div>
    </header>
    <footer class="footer">
      <p class="tagline">Wholesaler in Energy Optimization Product</p>
      <p class="product-line">Photovoltaics · LED · Heat Pumps · Jet Towels</p>
      <div class="partners">
        <span class="partner partner--tk"><span class="partner-dot"></span>TK</span>
        <span class="partner partner--brightmere">Brightmere Energy</span>
        <span class="partner partner--varnholt">Varnholt</span>
        <span class="partner partner--kestrel"><span class="partner-dot"></span>Kestrel</span>
        <span class="partner partner--lumora"><span class="partner-square"></span>Lumora</span>
      </div>
    </footer>
  </section>
</body>
</html>
```